Tobin Quartz Portal Page . It's guarantee project!

We need a clean and professional modern web application portal page
That includes the Login & Application Selection screen

Also, I need to design both Desktop and Mobile sizes.
We have an example design for our target

The application is Jetty Schedule and related data.
Our client is a bit conservative.

Theme color preferred : #00508B (main) #DF0D83 (secondary)

Target Market(s)

Oil & Fuel & Gasoline

Number of Pages Required

2 page

Font styles to use
Sans Serif

Colors
0054AA
0677BA
7BADD7
CADEEF
E8F1F8
E54698
E96AAD
F1A4CE
F9D9EA
FCEFF6

Requirements
Must have
• Login Page & Main Screen

```html
<!DOCTYPE html>
<html lang="en">
<head>
<meta charset="utf-8">
<title>Tobin Quartz – Login Page</title>
<link href="https://fonts.googleapis.com/css2?family=Montserrat:wght@400;500;600;700;800&display=swap" rel="stylesheet">
<style>
  :root{
    --navy:#00467d;
    --navy-deep:#003a6a;
    --brand-blue:#00508b;
    --pink:#df0d83;
    --sky:#1a8fe6;
    --sky-light:#3aa6f5;
    --ink:#1d2733;
    --muted:#9a9a9a;
    --label:#6f6f6f;
    --field-line:#d6d6d6;
    --caption:#8fa9c6;
    --white:#ffffff;
  }
  *{box-sizing:border-box;margin:0;padding:0}
  html,body{width:1200px;height:762px;overflow:hidden}
  body{
    font-family:'Montserrat',sans-serif;
    background:linear-gradient(160deg,#004c85 0%,var(--navy) 45%,var(--navy-deep) 100%);
    position:relative;
  }
  .corner-shapes{position:absolute;inset:0;width:1200px;height:762px}
  .board-title{
    position:absolute;left:70px;top:-2px;
    font-size:134px;font-weight:800;letter-spacing:-2px;
    color:rgba(255,255,255,.1);line-height:1;white-space:nowrap;
  }
  .section-caption{
    position:absolute;top:192px;font-size:25px;font-weight:400;
    color:var(--caption);letter-spacing:.3px;
  }
  .section-caption.desktop{left:146px}
  .section-caption.phone{left:863px}

  .card{position:absolute;top:248px;height:416px;border-radius:4px;overflow:hidden;background:var(--white)}
  .card.desktop{left:146px;width:640px}
  .card.phone{left:865px;width:192px}

  .hero{
    position:absolute;left:0;top:0;
    background:
      radial-gradient(ellipse at 70% 30%,rgba(120,200,255,.35),transparent 55%),
      radial-gradient(ellipse at 30% 80%,rgba(0,60,140,.45),transparent 60%),
      linear-gradient(155deg,#0a6fd0 0%,var(--sky) 35%,var(--sky-light) 60%,#0a5fb8 85%,#064a94 100%);
  }
  .desktop .hero{width:320px;height:416px}
  .phone .hero{width:192px;height:160px}

  .brand{position:absolute;display:flex;align-items:center;gap:6px;color:var(--white);font-weight:700}
  .brand-dot{width:12px;height:12px;border-radius:50%;background:var(--pink)}
  .desktop .brand{left:29px;top:40px;font-size:14px}
  .phone .brand{left:20px;top:30px;font-size:11px}
  .phone .brand-dot{width:10px;height:10px}

  .hero-greeting{position:absolute;font-weight:500;line-height:.93}
  .desktop .hero-greeting{left:29px;top:167px;font-size:46px;color:var(--white)}
  .phone .hero-greeting{left:20px;top:82px;font-size:24px;color:rgba(180,210,235,.55)}

  .form{position:absolute}
  .desktop .form{left:379px;top:52px;width:200px}
  .phone .form{left:0;top:160px;width:192px;height:256px}

  .form-title{font-weight:700;color:var(--brand-blue)}
  .desktop .form-title{font-size:23px;line-height:1}
  .phone .form-title{position:absolute;left:18px;top:10px;font-size:20px}
  .form-sub{margin-top:12px;font-size:7.6px;font-weight:600;color:var(--muted)}

  .field-label{display:block;color:var(--label);font-weight:400}
  .field{border:1px solid var(--field-line);border-radius:4px;background:var(--white);display:flex;align-items:center;color:var(--ink)}
  .desktop .field-label{font-size:13px;margin-top:27px}
  .desktop .field-label + .field{margin-top:6px}
  .desktop .field-label.second{margin-top:12px}
  .desktop .field{height:29px;padding-left:11px;font-size:8px}

  .phone .field-label{position:absolute;left:18px;font-size:12px}
  .phone .field{position:absolute;left:18px;width:156px;height:26px;padding-left:10px;font-size:7px}

  .options{display:flex;justify-content:space-between;align-items:center}
  .check{display:flex;align-items:center;gap:5px;color:var(--ink)}
  .check-box{width:9px;height:9px;border-radius:2px;background:var(--pink);display:flex;align-items:center;justify-content:center}
  .forgot{color:var(--muted);font-weight:600}
  .desktop .options{margin-top:16px;font-size:7.8px}
  .phone .options{position:absolute;left:18px;width:156px;top:402px;font-size:7px;top:242px}
  .phone .check-box{width:8px;height:8px}

  .login-btn{background:var(--pink);color:var(--white);font-weight:700;display:flex;align-items:center;justify-content:center}
  .desktop .login-btn{margin-top:17px;height:31px;border-radius:3px;font-size:8px}
  .phone .login-btn{position:absolute;left:0;width:192px;top:270px;height:27px;font-size:7px}

  .signup{color:var(--label)}
  .signup strong{color:var(--pink);font-weight:700;margin-left:3px}
  .desktop .signup{margin-top:26px;font-size:7.8px}
  .phone .signup{position:absolute;left:10px;top:227px;font-size:7px}
</style>
</head>
<body>
  <svg class="corner-shapes" viewBox="0 0 1200 762" aria-hidden="true">
    <circle cx="1330" cy="-120" r="275" fill="#df0d83"/>
    <circle cx="-140" cy="900" r="310" fill="#df0d83"/>
  </svg>

  <div class="board-title">Login page</div>
  <div class="section-caption desktop">Desktop Version</div>
  <div class="section-caption phone">Phone Version</div>

  <section class="card desktop">
    <div class="hero" role="img" aria-label="Abstract fluid blue marble texture background">
      <div class="brand"><span class="brand-dot"></span>Tobin Quartz</div>
      <div class="hero-greeting">Welcome<br>Back!</div>
    </div>
    <form class="form">
      <h1 class="form-title">Login</h1>
      <p class="form-sub">Welcome back! Please login to your account.</p>
      <label class="field-label">Email</label>
      <div class="field">username@mailbox.com</div>
      <label class="field-label second">Password</label>
      <div class="field">****************</div>
      <div class="options">
        <span class="check"><span class="check-box"><svg width="6" height="5" viewBox="0 0 6 5"><path d="M.6 2.5 2.3 4 5.4.8" fill="none" stroke="#fff" stroke-width="1.1"/></svg></span>Remember me</span>
        <span class="forgot">Forgot password</span>
      </div>
      <div class="login-btn">Login</div>
      <p class="signup">New User?<strong>Signup</strong></p>
    </form>
  </section>

  <section class="card phone">
    <div class="hero" role="img" aria-label="Abstract fluid blue marble texture background">
      <div class="brand"><span class="brand-dot"></span>Tobin Quartz</div>
      <div class="hero-greeting">Welcome<br>Back!</div>
    </div>
    <form class="form">
      <h1 class="form-title">Login</h1>
      <label class="field-label" style="top:39px">Email</label>
      <div class="field" style="top:61px">username@mailbox.com</div>
      <label class="field-label" style="top:94px">Password</label>
      <div class="field" style="top:116px">****************</div>
      <div class="options" style="top:162px">
        <span class="check"><span class="check-box"><svg width="5" height="4" viewBox="0 0 6 5"><path d="M.6 2.5 2.3 4 5.4.8" fill="none" stroke="#fff" stroke-width="1.1"/></svg></span>Remember me</span>
        <span class="forgot">Forgot password</span>
      </div>
      <div class="login-btn" style="top:182px">Login</div>
      <p class="signup" style="top:226px">New User?<strong>Signup</strong></p>
    </form>
  </section>
</body>
</html>
```